Caldwen Primary School

We need to improve on our designs for a local School, Caldwen Primary.
One file contains the correct information required on the sign.
Our Mock ups are suggestions.
The School Uniform is blue -
We had these comments from our Client.
I can't decide whether to change the blue and try green to represent our commitment to outdoors, or maybe a combination of colours from the school badge, For the main sign options , I like them both but wondered if there was a way of combining the two? Slightly bigger badge.

I've included the files for the smaller signs if you were happy to provide a service to include all. We are a sign business focusing on other projects and external support will help. Thanks - Oscar.

```html
<!DOCTYPE html>
<html lang="en">
<head>
<meta charset="utf-8">
<title>Caldwen Primary School – Entrance Sign</title>
<link rel="stylesheet" href="https://fonts.googleapis.com/css2?family=Montserrat:wght@600;700;800&display=swap">
<style>
  :root {
    --sign-blue: #2171b9;
    --frame-white: #ffffff;
    --greeting-yellow: #f8dc4d;
    --meadow-light: #9bc646;
    --meadow-dark: #2f8557;
    --page-bg: #ffffff;
  }
  html, body {
    margin: 0;
    padding: 0;
    width: 1200px;
    height: 805px;
    overflow: hidden;
    background: var(--page-bg);
  }
  .sign {
    display: block;
    width: 1200px;
    height: 805px;
    font-family: "Montserrat", sans-serif;
  }
  .sign-body { fill: var(--sign-blue); }
  .sign-frame { fill: none; stroke: var(--frame-white); stroke-width: 16; }
  .hill-highlight { fill: var(--frame-white); }
  .hill-sky { fill: var(--sign-blue); }
  .hill-light { fill: var(--meadow-light); }
  .hill-dark { fill: var(--meadow-dark); }
  .badge-disc { fill: var(--frame-white); }
  .badge-name { fill: var(--sign-blue); font-weight: 800; font-size: 74px; }
  .greeting { fill: var(--greeting-yellow); font-weight: 600; font-size: 96px; }
  .greeting-bar { fill: var(--greeting-yellow); }
  .school-name { fill: var(--frame-white); font-weight: 700; font-size: 176px; }
  .motto { fill: var(--frame-white); font-weight: 700; font-size: 96px; }
  .phone-ring { fill: none; stroke: var(--frame-white); stroke-width: 8; }
  .phone-glyph { fill: var(--frame-white); }
  .phone-number { fill: var(--frame-white); font-weight: 700; font-size: 96px; }
</style>
</head>
<body>
<svg class="sign" viewBox="0 0 2334 1567" preserveAspectRatio="none" xmlns="http://www.w3.org/2000/svg" role="img" aria-label="Caldwen Primary School entrance sign">
  <defs>
    <clipPath id="inner-panel">
      <path d="M100 482 L670 482 C770 482 790 430 820 350 C890 170 1020 115 1165 115 C1320 115 1460 200 1530 370 C1560 440 1580 482 1690 482 L2230 482 C2260 482 2262 500 2262 530 L2262 1400 C2262 1440 2245 1445 2210 1445 L110 1445 C80 1445 75 1430 75 1400 L75 520 C75 490 85 482 100 482 Z"/>
    </clipPath>
  </defs>

  <path class="sign-body" d="M100 450 L660 452 C760 450 760 400 790 330 C870 140 1020 80 1160 80 C1320 80 1480 170 1560 360 C1600 450 1600 452 1680 452 L2240 450 C2280 450 2295 480 2295 510 L2295 1420 C2295 1460 2270 1482 2220 1482 L100 1482 C60 1482 40 1460 40 1420 L40 520 C40 480 60 450 100 450 Z"/>

  <g class="landscape" clip-path="url(#inner-panel)">
    <path class="hill-highlight" d="M60 1135 C500 1205 1100 1160 1500 1132 C1900 1110 2100 1125 2280 1150 L2280 1600 L60 1600 Z"/>
    <path class="hill-sky" d="M60 1160 C500 1215 1000 1185 1500 1140 C1900 1140 2100 1165 2280 1195 L2280 1600 L60 1600 Z"/>
    <path class="hill-light" d="M60 1190 C500 1230 1000 1200 1500 1135 C1900 1140 2100 1190 2280 1235 L2280 1600 L60 1600 Z"/>
    <path class="hill-dark" d="M60 1258 C600 1290 1200 1200 1500 1195 C1800 1200 2000 1280 2280 1342 L2280 1600 L60 1600 Z"/>
  </g>

  <path class="sign-frame" d="M100 482 L670 482 C770 482 790 430 820 350 C890 170 1020 115 1165 115 C1320 115 1460 200 1530 370 C1560 440 1580 482 1690 482 L2230 482 C2260 482 2262 500 2262 530 L2262 1400 C2262 1440 2245 1445 2210 1445 L110 1445 C80 1445 75 1430 75 1400 L75 520 C75 490 85 482 100 482 Z"/>

  <g class="badge">
    <circle class="badge-disc" cx="1173" cy="413" r="245"/>
    <text class="badge-name" x="1173" y="440" text-anchor="middle">Caldwen</text>
  </g>

  <g class="greetings">
    <text class="greeting" x="270" y="628">Welcome</text>
    <rect class="greeting-bar" x="781" y="543" width="12" height="105"/>
    <rect class="greeting-bar" x="1553" y="543" width="12" height="105"/>
    <text class="greeting" x="1593" y="628" lang="cy">Croeso</text>
  </g>

  <text class="school-name" x="188" y="870" textLength="1960" lengthAdjust="spacingAndGlyphs">Caldwen Primary School</text>
  <text class="motto" x="390" y="1035" textLength="1555" lengthAdjust="spacingAndGlyphs">“Wings to Fly, Roots to Grow”</text>

  <g class="contact">
    <circle class="phone-ring" cx="822" cy="1313" r="52"/>
    <path class="phone-glyph" transform="translate(779 1270) scale(3.6)" d="M6.6 10.8c1.4 2.8 3.8 5.1 6.6 6.6l2.2-2.2c.3-.3.7-.4 1-.2 1.1.4 2.3.6 3.6.6.6 0 1 .4 1 1V20c0 .6-.4 1-1 1C10.6 21 3 13.4 3 4c0-.6.4-1 1-1h3.5c.6 0 1 .4 1 1 0 1.3.2 2.5.6 3.6.1.3 0 .7-.2 1z"/>
    <text class="phone-number" x="897" y="1350" textLength="675" lengthAdjust="spacingAndGlyphs">01632 960418</text>
  </g>
</svg>
</body>
</html>
```